Website design improvement for existing site

We would like design ideas for how the inner pages (not the homepage) of www.quillbrookmedia.com could be improved. We don't want to totally redesign the website. We want to improve / enhance / develop it further to look high-end, sophisticated and visually stunning.

Target Market(s)

High end video production clients. National and international TV networks and brands wanting commercial filming.

Industry/Entity Type

Videography

Other font styles liked:
• Existing site fonts

Requirements
Must have
• Improvement on the existing inner pages without totally re-working the design. We want to achieve a high-end sophisticated look with the existing branding (colours, images etc)
Nice to have
• Any ideas for improving the homepage are also welcome but we are mostly happy with this page so it is not the priority.
Should not have
• Any major changes to colours, styles etc.

```html
<!DOCTYPE html>
<html lang="en">
<head>
<meta charset="utf-8">
<title>Quillbrook Media – About</title>
<link href="https://fonts.googleapis.com/css2?family=Fira+Mono&family=Mulish:wght@400;600&display=swap" rel="stylesheet">
<style>
  :root {
    --backdrop: #e4e4e3;
    --page: #ffffff;
    --ink: #2a2a2a;
    --footer: #000000;
    --footer-ink: #ffffff;
    --hero-dark: #3b3f47;
    --hero-mid: #7d8aa6;
    --hero-light: #d9dde4;
    --violet: #6a2f8e;
    --magenta: #e0157f;
    --red: #c8102e;
    --charcoal: #333333;
    --olive: #5b7f2a;
    --teal: #1aa7c0;
  }
  * { margin: 0; padding: 0; box-sizing: border-box; }
  html, body { width: 1200px; height: 1200px; overflow: hidden; }
  body {
    background: var(--backdrop);
    display: flex;
    align-items: center;
    justify-content: center;
  }
  .site {
    width: 1200px;
    height: 856px;
    background: var(--page);
    display: flex;
    flex-direction: column;
  }
  .hero {
    height: 180px;
    background: linear-gradient(100deg, var(--hero-dark) 0%, var(--hero-mid) 35%, #5a6f9c 50%, var(--hero-light) 75%, #8d8f94 100%);
  }
  .intro {
    flex: 1;
    position: relative;
  }
  .intro-text {
    position: absolute;
    left: 450px;
    top: 54px;
    width: 560px;
    font-family: "Fira Mono", monospace;
    font-size: 14px;
    line-height: 24px;
    color: var(--ink);
  }
  .clients {
    position: absolute;
    top: 240px;
    left: 0;
    right: 0;
    display: flex;
    justify-content: center;
    align-items: center;
    gap: 30px;
  }
  .client {
    display: flex;
    align-items: center;
    gap: 8px;
    font-family: "Fira Mono", monospace;
    font-size: 17px;
    white-space: nowrap;
  }
  .client-mark { width: 14px; height: 14px; flex: none; }
  .client-mark.round { border-radius: 50%; }
  .client--northvale { color: var(--violet); }
  .client--northvale .client-mark { background: var(--violet); }
  .client--brightmere { color: var(--magenta); }
  .client--harbour { color: var(--red); }
  .client--harbour .client-mark { background: var(--red); }
  .client--kestrel { color: var(--charcoal); }
  .client--elm { color: var(--olive); }
  .client--elm .client-mark { background: var(--olive); }
  .client--tern { color: var(--teal); }
  .footer {
    height: 222px;
    background: var(--footer);
    color: var(--footer-ink);
    font-family: "Mulish", sans-serif;
    text-align: center;
    padding-top: 40px;
  }
  .social {
    display: flex;
    justify-content: center;
    gap: 22px;
    font-weight: 600;
    font-size: 14px;
    letter-spacing: 1px;
    margin-bottom: 32px;
  }
  .company-details {
    font-size: 11px;
    line-height: 20px;
    letter-spacing: 1.2px;
  }
</style>
</head>
<body>
  <main class="site">
    <div class="hero" role="img" aria-label="Photo of a field monitor showing a food shot on a kitchen set"></div>
    <section class="intro">
      <p class="intro-text">Rowan  collaborates with a team of skilled pre-production, production &amp; post-production specialists from Leeds and York to London. He’s worked with some of the UK’s biggest creative agencies and helped tell the brand stories of companies of all sizes and sectors, working with both agencies and businesses.</p>
      <div class="clients">
        <div class="client client--northvale"><span class="client-mark"></span>Northvale</div>
        <div class="client client--brightmere">Brightmere</div>
        <div class="client client--harbour"><span class="client-mark round"></span>Harbour Nine</div>
        <div class="client client--kestrel">Kestrel Pictures</div>
        <div class="client client--elm">Elm Advisory<span class="client-mark round"></span></div>
        <div class="client client--tern">Tern TV</div>
      </div>
    </section>
    <footer class="footer">
      <div class="social">
        <span>Linkstream</span>
        <span>Pixgram</span>
      </div>
      <div class="company-details">
        <p>Quillbrook Media Ltd</p>
        <p>01632 960418 | hello@quillbrookmedia.com</p>
        <p>Company No. 12345678</p>
        <p>VAT No. 987654321</p>
      </div>
    </footer>
  </main>
</body>
</html>
```